Web Design Project

We need a website design for our marketing agency: clearvane.com.au

We want something that is eye-catching and will wow audiences, yet at the same time it cannot turn-off corporate clients. The website should be highly focused on conversions with numerous call to actions on each page.

We like blue as our primary colour and have a mascot (the spider on the current website)

Target Market(s)

small business owners
small corporations
enterprise level business clients

Industry/Entity Type

Marketing

Requirements
Must have
• must incorporate the agency mascot (the spider on the website)

```html
<!DOCTYPE html>
<html lang="en">
<head>
<meta charset="utf-8">
<title>Clearvane – High ROI Digital Marketing</title>
<link rel="stylesheet" href="https://fonts.googleapis.com/css2?family=Gelasio:wght@400;700&family=Anton&display=swap">
<style>
:root{
  --sky-top:#6fa3e6;
  --sky-bottom:#3d7be0;
  --page:#ffffff;
  --header-top:#ffffff;
  --header-bottom:#dbe9fb;
  --band:#f2f4f7;
  --ink:#3a3a3a;
  --ink-soft:#555;
  --heading:#333;
  --accent:#3b6db3;
  --nav-active:#2f6fd0;
  --nav-line:#9aa8bb;
  --rule:#c9ced6;
  --field:#ffffff;
}
*{box-sizing:border-box;margin:0;padding:0}
html,body{width:715px;height:1200px;overflow:hidden}
body{background:linear-gradient(180deg,var(--sky-top),var(--sky-bottom));font-family:"Gelasio",Georgia,serif;color:var(--ink);position:relative}
.page{position:absolute;left:69px;top:36px;width:577px;height:1126px;background:linear-gradient(180deg,#fff 0,#fff 330px,#eaf2fc 560px,#fff 900px,#e6f0fc 1100px);}
.abs{position:absolute}
/* header */
.site-header{left:0;top:0;width:577px;height:196px;background:linear-gradient(180deg,var(--header-top),var(--header-bottom));border-bottom:3px solid var(--rule)}
.brand{left:32px;top:-4px;font-family:"Anton",sans-serif;font-size:46px;letter-spacing:2px;color:#4a7fd0;line-height:1}
.tagline{left:141px;top:62px;font-family:"Anton",sans-serif;font-size:17px;letter-spacing:1px;color:#3b6fc4}
.web-art{left:262px;top:6px;width:310px;height:176px;border-radius:50% 50% 10px 10px;background:radial-gradient(ellipse at 70% 40%,rgba(150,160,180,.35),rgba(150,160,180,0) 70%)}
.mascot{left:420px;top:6px;width:122px;height:134px;border-radius:50%;background:radial-gradient(circle at 50% 50%,#c7ccd6,#8e96a6 70%,rgba(142,150,166,0) 72%)}
.nav{left:1px;top:117px;height:70px;display:flex}
.nav a{display:flex;align-items:center;padding:0 3px;height:70px;font-size:8.5px;color:#222;text-decoration:none;border-right:1px solid var(--nav-line);letter-spacing:.2px}
.nav a.active{background:linear-gradient(180deg,#5a93e6,var(--nav-active));color:#fff;width:36px;justify-content:center;border-radius:0 0 3px 3px}
/* feature band */
.features{left:0;top:199px;width:577px;height:129px;background:var(--band)}
.feature{position:absolute;top:13px;width:165px}
.feature-icon{position:absolute;left:0;top:0;width:30px;height:30px;border-radius:5px;background:linear-gradient(180deg,#e8ecf2,#b9c3d2)}
.feature h3{position:absolute;left:34px;top:20px;font-size:9px;color:var(--accent);font-weight:700;white-space:nowrap}
.feature p{position:absolute;left:0;top:44px;width:165px;font-size:6.6px;line-height:10px;text-align:justify;color:var(--ink-soft)}
/* services */
.service{left:0;width:577px}
.service-art{position:absolute;left:56px;width:92px;height:80px;border-radius:8px}
.service h2{position:absolute;left:202px;top:0;font-size:10.5px;font-weight:700;color:var(--heading)}
.service p{position:absolute;left:202px;width:357px;font-size:6.4px;line-height:10.5px;text-align:justify;color:var(--ink-soft)}
/* form */
.audit-intro{left:22px;top:938px;width:185px;font-size:8.6px;line-height:11px;color:var(--ink)}
.audit-form label{position:absolute;left:22px;font-size:7.6px;color:var(--ink)}
.audit-form .field{position:absolute;left:114px;width:83px;height:13px;background:var(--field);border:none}
.cta{left:89px;top:1085px;width:108px;height:12px;background:linear-gradient(180deg,#fff,#dfe3e8);border:1px solid #aab;font-size:6.6px;letter-spacing:.6px;text-align:center;line-height:10px;color:#333}
.address{right:20px;top:1030px;text-align:right;font-size:7.2px;line-height:10.5px;color:var(--ink)}
.address strong{font-weight:700}
.phone{right:20px;top:1088px;font-size:9.6px;color:var(--ink)}
.site-footer{left:0;top:1108px;width:577px;height:18px;background:#eef2f7;font-size:6.4px;color:#444}
.site-footer span{position:absolute;top:5px}
</style>
</head>
<body>
<div class="page">

  <header class="site-header abs">
    <div class="web-art abs" role="img" aria-label="Spider web illustration"></div>
    <div class="mascot abs" role="img" aria-label="Robot spider mascot"></div>
    <div class="brand abs">CLEARVANE</div>
    <div class="tagline abs">HIGH ROI DIGITAL MARKETING</div>
    <nav class="nav abs">
      <a class="active" href="#">HOME</a>
      <a href="#">SERVICES</a>
      <a href="#">BLOG</a>
      <a href="#">SEO PRICING</a>
      <a href="#">SEM</a>
      <a href="#">ABOUT CLEARVANE</a>
      <a href="#">CONTACT CLEARVANE</a>
    </nav>
  </header>

  <section class="features abs">
    <div class="feature" style="left:22px">
      <div class="feature-icon" role="img" aria-label="Ad management icon"></div>
      <h3>Online Ad Management</h3>
      <p>Need highly targeted traffic right now? Then let us help! We have a whole range of online advertising solutions, from Searchly Ads to Friendlane Ads to interactive banner Ads. Ad copy, creatives design &amp; conversion optimization – we can handle everything and get you the highest ROI for your ad dollar.</p>
    </div>
    <div class="feature" style="left:210px">
      <div class="feature-icon" role="img" aria-label="Social media icon"></div>
      <h3>Social Media</h3>
      <p>Need to engage your target market? Want build your brand to create a loyal base of supporters for your business? Then social media is your solution. We can advise which social media options are right for your business – and there are way more options than just Friendlane and Chirper!</p>
    </div>
    <div class="feature" style="left:402px">
      <div class="feature-icon" role="img" aria-label="SEO packages icon"></div>
      <h3>SEO Packages</h3>
      <p>Drive quality traffic to your business and boost your revenue. We offer high quality SEO packages at competitive rates with GUARANTEED results. Whether you're a local business or a national enterprise, we can help your business grow.</p>
    </div>
  </section>

  <section class="service abs" style="top:350px">
    <div class="service-art" style="top:22px;background:linear-gradient(90deg,#f7a040,#7b6ee8,#3cc84a)" role="img" aria-label="Colourful bar chart with magnifying glass"></div>
    <h2>Clearvane Digital Marketing</h2>
    <p style="top:20px">search engine optimisationOnline marketing channels are a major factor almost any business. Clearvane is a digital marketing agency focused on results and ROI. Whether its search engine optimisation with our advanced SEO services or Pay-Per-Click search engine marketing (SEM) – we are here to help you achieve your business goals with our range of results-oriented marketing solutions.<br><br>Clearvane accepts clients big and small – whether you're an international corporation needing to boost seasonal sales with multi-platform online ad campaign, a government department trying to raise public awareness, or an electrical contractor needing SEO Brisbane. We are a digital agency that actually cares about your business and would love to help you grow.</p>
  </section>

  <section class="service abs" style="top:485px">
    <div class="service-art" style="top:14px;left:52px;width:110px;height:86px;background:linear-gradient(135deg,#e9ecf1,#c6ccd6)" role="img" aria-label="Search engine cubes spelling SEO"></div>
    <h2>Search Engine Optimisation</h2>
    <p style="top:20px">SEO BrisbaneA website without traffic is useless. Traffic is the commodity of the internet: driving information &amp; business in our online economy. You don't need to have an online store to benefit from search engine optimisation. Studies show that almost 66% of purchases (offline and online together) start with the consumer looking for information on a search engine.<br><br>Ignoring your search visibility and rankings can hurt the growth and success of your business. Business today cannot afford online obscurity – you may as well send customers to your competitors. We can help your business increase its revenue and reach via a range of online marketing channels – get in contact now to find out how. Clearvane offers the best international, national and Brisbane SEO services.</p>
  </section>

  <section class="service abs" style="top:620px">
    <div class="service-art" style="top:-10px;left:70px;width:62px;height:80px;background:linear-gradient(160deg,#e03a2a,#f2a62a,#3a9ad8)" role="img" aria-label="Rising arrows with dollar sign"></div>
    <h2>SEO Services</h2>
    <p style="top:20px">SEO ServicesIt's not just about quantity of traffic but quality. Clearvane's SEO services can drive targeted traffic to your site maximizing your visibility and increasing revenue. We offer a range of high quality SEO services with guaranteed results. We can help increase your sales, brand visibility and revenue whether you are a nationwide institution that needs a scalable search engine optimisation campaign or are a local business needing just SEO Brisbane or Sydney.</p>
  </section>

  <section class="service abs" style="top:713px">
    <div class="service-art" style="top:-10px;left:70px;width:62px;height:80px;background:linear-gradient(160deg,#e05a2a,#5cc03a,#2f6ed0)" role="img" aria-label="Rising arrows above SEO letters"></div>
    <h2>SEO Brisbane</h2>
    <p style="top:20px">Brisbane SEO ServicesNeed Brisbane SEO services? We can help! Clearvane is located in Brisbane, Australia and service clients Australia wide &amp; overseas. We started off as Clearvane SEO Brisbane and now offer search engine marketing (SEM services), social media consulting and more. For the best search engine optimisation Brisbane, Australia or anywhere get in contact with us now to find out how we can help your business grow.</p>
  </section>

  <section class="service abs" style="top:807px">
    <div class="service-art" style="top:8px;left:62px;width:80px;height:72px;background:radial-gradient(circle at 60% 60%,#c8352c,#8c9a3c 55%,rgba(140,154,60,0) 72%)" role="img" aria-label="Gears diagram of traffic, visibility and conversions"></div>
    <h2>SEM Services</h2>
    <p style="top:20px">SEM ServicesHigh ROI online advertising is a speciality of ours. Effectively managing search engine marketing campaigns takes a lot of time, experience and expertise. The results of subpar SEM services can leave a big hole in your pocket with little return.<br><br>Quality SEM Services are based constant analysis, testing and refinement of ads, landing pages, conversion funnels and overall advertising strategy. Clearvane uses a methodical, scientific approach to search engine marketing focused on maximizing conversions and minimizing CPA (cost per acquisition). To find out more see our PPC Services.</p>
  </section>

  <p class="audit-intro abs">Fill in your details to get an SEO Audit (worth $500) to improve your website's performance. It's FREE but only until December 30!</p>
  <form class="audit-form">
    <label style="top:985px">Name</label><input class="field" style="top:983px" aria-label="Name">
    <label style="top:1005px">Email</label><input class="field" style="top:1003px" aria-label="Email">
    <label style="top:1025px">Phone</label><input class="field" style="top:1023px" aria-label="Phone">
    <label style="top:1045px">Website URL</label><input class="field" style="top:1043px" aria-label="Website URL">
    <label style="top:1065px">Leave This Field Empty</label><input class="field" style="top:1063px" aria-label="Leave empty">
    <div class="cta abs">ORDER YOUR FREE REPORT</div>
  </form>

  <address class="address abs" style="font-style:normal"><strong>Address :</strong><br>Level 36,<br>Harbourline Plaza,<br>48 Kestrel Street,<br>Brisbane, Qld, 4000</address>
  <div class="phone abs">Call Us Now (+617) 3000 4812</div>

  <footer class="site-footer abs">
    <span style="left:22px">Copyright © All rights reserved by Clearvane</span>
    <span style="right:20px">Designed by Patchwork Studio</span>
  </footer>
</div>
</body>
</html>
```